Presentation Folder

Design presentation folder for professional law firm. Our law firm primarily represents individuals who are dealing with divorce, child custody, child support, spousal support, wills, estates and other civil litigation.
We desire a simple, professional, but memorable presentation folder that we can give clients containing their important documents (e.g., contract, and other important papers). The folder will also have a place for a business card. We will print this at Plumcrest. Specs and Templates are available at http://www.plumcrest-example.com/vp/ns/propath/UploadResources.aspx?selectedTab=0?pfid=156&pf_id=156&xnav=studio-side-bar#Templates
Our logo and one of our business cards is attached.
Our website is www.MorrowFamilyLaw-example.com
Target Market(s)
Individual with legal issues primarily undergoing divorce
Industry/Entity Type
Law Firm
Font styles to use
Other font styles liked:
- Tahoma
Look and feel
Each slider illustrates characteristics of the customer's brand and the style your logo design should communicate.

```html
<!DOCTYPE html>
<html lang="en">
<head>
<meta charset="utf-8">
<title>Morrow Law Firm — Presentation Folder</title>
<link rel="stylesheet" href="https://fonts.googleapis.com/css2?family=PT+Sans:wght@400;700&display=swap">
<style>
  :root {
    --backdrop: #ececec;
    --folder-navy: #2b3266;
    --accent-gold: #e3b62a;
    --logo-panel: #f4ecdc;
    --logo-ink: #2b3266;
  }
  * { box-sizing: border-box; margin: 0; padding: 0; }
  html, body {
    width: 1200px;
    height: 1000px;
    overflow: hidden;
    background: var(--backdrop);
    font-family: "PT Sans", Tahoma, sans-serif;
  }
  .canvas {
    position: relative;
    width: 1200px;
    height: 1000px;
  }
  .folder-cover {
    position: absolute;
    left: 300px;
    top: 90px;
    width: 600px;
    height: 820px;
    background: var(--folder-navy);
    box-shadow: 0 6px 18px rgba(0,0,0,0.18);
  }
  .brand-mark {
    position: absolute;
    top: 70px;
    left: 50%;
    transform: translateX(-50%);
    width: 170px;
    height: 150px;
    background: var(--logo-panel);
    display: flex;
    flex-direction: column;
    align-items: center;
    justify-content: center;
    gap: 12px;
  }
  .brand-mark__square {
    width: 34px;
    height: 34px;
    background: var(--logo-ink);
  }
  .brand-mark__name {
    color: var(--logo-ink);
    font-size: 20px;
    font-weight: 700;
    letter-spacing: 0.04em;
    text-align: center;
    line-height: 1.15;
  }
  .cover-tagline {
    position: absolute;
    right: 40px;
    bottom: 48px;
    color: var(--accent-gold);
    font-size: 15px;
    line-height: 1.3;
    text-align: right;
    letter-spacing: 0.02em;
  }
  .cover-band {
    position: absolute;
    left: 0;
    right: 0;
    bottom: 0;
    height: 16px;
    background: var(--accent-gold);
  }
</style>
</head>
<body>
  <main class="canvas">
    <section class="folder-cover" aria-label="Presentation folder front cover">
      <div class="brand-mark">
        <span class="brand-mark__square" aria-hidden="true"></span>
        <span class="brand-mark__name">Morrow<br>Law Firm</span>
      </div>
      <p class="cover-tagline">Supporting your family in times<br>of tumult and transition.</p>
      <div class="cover-band" aria-hidden="true"></div>
    </section>
  </main>
</body>
</html>
```